Brixel capital

We lend hard money loans for fixer upper homes and new constructions.Easy Financing on Fix Homes

Target Market(s)

People that need loans & money to buy a Home

Industry/Entity Type

Mortgage Lender

Font styles to use
Serif
Sans Serif

Colors
ffffff
9ccb3b

Requirements
Must have
• Catchy, modern, Clean
Nice to have
• Easy to read

```html
<!DOCTYPE html>
<html lang="en">
<head>
<meta charset="utf-8">
<title>Brixel capital – Business Cards</title>
<link rel="stylesheet" href="https://fonts.googleapis.com/css2?family=Arimo:wght@400;700&display=swap">
<style>
  :root {
    --green: #9ccb3b;
    --green-light: #b9d33f;
    --green-deep: #7aab3e;
    --green-text: #86b23a;
    --white: #ffffff;
    --paper: #f7f7f7;
    --ink: #2b2b2b;
    --ink-soft: #444444;
    --backdrop-top: #d9d9db;
    --backdrop-bottom: #bdbdbf;
  }
  * { box-sizing: border-box; margin: 0; padding: 0; }
  html, body {
    width: 1200px;
    height: 990px;
    overflow: hidden;
  }
  body {
    background: linear-gradient(180deg, var(--backdrop-top), var(--backdrop-bottom));
    font-family: "Arimo", Arial, sans-serif;
    position: relative;
  }
  .card-row {
    position: absolute;
    top: 345px;
    left: 50px;
    width: 1100px;
    display: flex;
    justify-content: space-between;
  }
  .card {
    position: relative;
    width: 540px;
    height: 300px;
    border-radius: 16px;
    overflow: hidden;
    background: var(--paper);
    box-shadow: 0 4px 8px rgba(0,0,0,0.25);
  }
  .card-surface {
    position: absolute;
    inset: 0;
    width: 100%;
    height: 100%;
  }
  .brand-mark {
    position: absolute;
    text-align: center;
    color: var(--ink);
    font-weight: 700;
    line-height: 1;
  }
  .brand-name { display: block; }
  .brand-sub { display: block; letter-spacing: 0.55em; }
  .card--front .brand-mark { left: 315px; top: 210px; width: 170px; }
  .card--front .brand-name { font-size: 36px; }
  .card--front .brand-sub { font-size: 14px; margin-top: 3px; padding-left: 0.55em; }
  .card--back .brand-mark { left: 175px; top: 205px; width: 190px; }
  .card--back .brand-name { font-size: 38px; }
  .card--back .brand-sub { font-size: 14px; margin-top: 3px; padding-left: 0.55em; }

  .contact {
    position: absolute;
    left: 39px;
    top: 112px;
    color: var(--ink-soft);
  }
  .contact-name {
    font-size: 17px;
    font-weight: 700;
    color: var(--green-text);
    letter-spacing: 0.01em;
  }
  .contact-title { font-size: 12px; margin-top: 4px; }
  .contact-lines { list-style: none; margin-top: 40px; font-size: 12px; line-height: 18px; }
  .contact-lines .label { color: var(--green-text); font-weight: 700; }
  .contact-lines .accent { color: var(--green-text); font-weight: 700; }
  .contact-address { font-size: 12px; margin-top: 15px; }
</style>
</head>
<body>
  <main class="card-row">
    <!-- Contact side -->
    <section class="card card--front">
      <svg class="card-surface" viewBox="0 0 540 300" aria-hidden="true">
        <defs>
          <linearGradient id="front-green" x1="0" y1="0" x2="1" y2="0">
            <stop offset="0" stop-color="#b9d33f"/>
            <stop offset="1" stop-color="#7aab3e"/>
          </linearGradient>
        </defs>
        <rect width="540" height="300" fill="url(#front-green)"/>
        <path d="M0 62 C120 20 250 25 370 60 C440 80 500 110 540 120" fill="none" stroke="#c6de6a" stroke-width="3" opacity="0.7"/>
        <path d="M0 70 C120 30 260 35 380 72 C450 92 505 125 540 135" fill="none" stroke="#cfe37d" stroke-width="2" opacity="0.6"/>
        <path d="M0 86 C110 45 250 45 360 78 C440 100 500 140 540 160 L540 300 L0 300 Z" fill="#f7f7f7"/>
        <circle cx="400" cy="140" r="72" fill="#f7f7f7"/>
      </svg>
      <div class="contact">
        <p class="contact-name">JORDAN MERCER</p>
        <p class="contact-title">General Manager</p>
        <ul class="contact-lines">
          <li><span class="label">T:</span> (555) 014-2286</li>
          <li><span class="label">E:</span> info@brixelcapitallend.com</li>
          <li>www.<span class="accent">brixelcapitallend</span>.com</li>
        </ul>
        <p class="contact-address">48 Harbor Ave., Easton, NY 10090</p>
      </div>
      <div class="brand-mark" aria-label="Brixel capital">
        <span class="brand-name">Brixel</span>
        <span class="brand-sub">CAPITAL</span>
      </div>
    </section>

    <!-- Brand side -->
    <section class="card card--back">
      <svg class="card-surface" viewBox="0 0 540 300" aria-hidden="true">
        <defs>
          <linearGradient id="back-green" x1="0" y1="0" x2="1" y2="0">
            <stop offset="0" stop-color="#b9d33f"/>
            <stop offset="1" stop-color="#7aab3e"/>
          </linearGradient>
        </defs>
        <rect width="540" height="300" fill="url(#back-green)"/>
        <path d="M0 140 C80 120 160 110 270 120 C380 130 460 170 540 200" fill="none" stroke="#c6de6a" stroke-width="3" opacity="0.7"/>
        <path d="M0 150 C90 128 170 122 280 132 C390 144 470 185 540 212" fill="none" stroke="#cfe37d" stroke-width="2" opacity="0.6"/>
        <path d="M0 160 C90 135 180 130 280 142 C390 156 470 195 540 222 L540 300 L0 300 Z" fill="#f7f7f7"/>
        <circle cx="270" cy="122" r="84" fill="#f7f7f7"/>
      </svg>
      <div class="brand-mark" aria-label="Brixel capital">
        <span class="brand-name">Brixel</span>
        <span class="brand-sub">CAPITAL</span>
      </div>
    </section>
  </main>
</body>
</html>
```